Mosk trail Website

We need a simple web page design for our businessWe procure and dispose of earthmoving construction equipmentwe also find construction equipment for our customers using our global contacts

Number of Pages Required

1 page

```html
<!DOCTYPE html>
<html lang="en">
<head>
<meta charset="utf-8">
<title>Mosk trail</title>
<link rel="stylesheet" href="https://fonts.googleapis.com/css2?family=Montserrat:wght@400;600;700&family=Open+Sans:wght@400;600&family=Merriweather:ital@1&display=swap">
<style>
:root{
  --bg:#272727;
  --bg-dark:#222;
  --orange:#f4a62a;
  --white:#fff;
  --line:#8a8a8a;
  --star:#ffd21f;
}
*{box-sizing:border-box;margin:0;padding:0}
html,body{width:1200px;height:2639px;overflow:hidden}
body{background:var(--bg);color:var(--white);font-family:"Open Sans",sans-serif;font-size:13px;line-height:1.5}
.page{width:1200px;height:2639px;position:relative}
section,footer{position:relative;width:1200px;overflow:hidden}
.container{width:1012px;margin:0 auto;position:relative;height:100%}
.section-title{font-family:"Montserrat",sans-serif;font-weight:700;font-size:34px;line-height:1.2;letter-spacing:3px;text-align:center}

/* hero */
.hero{height:503px}
.hero-photo{position:absolute;inset:0;background:radial-gradient(ellipse 300px 230px at 50% 40%,#e8a23c 0%,#a05a14 35%,#3a2510 70%,#141210 100%)}
.nav{position:absolute;top:22px;left:94px;right:94px;display:flex;justify-content:space-between;align-items:center}
.brand{font-family:"Montserrat",sans-serif;font-weight:600;font-size:19px}
.nav-links{display:flex;gap:20px;list-style:none;font-family:"Montserrat",sans-serif;font-size:13px;color:#e6e6e6}
.hero-copy{position:absolute;top:265px;left:0;right:0;text-align:center}
.hero-kicker{font-family:"Merriweather",serif;font-style:italic;font-size:30px;line-height:38px;letter-spacing:1px}
.hero-title{font-family:"Montserrat",sans-serif;font-weight:700;font-size:60px;line-height:68px;letter-spacing:2px}
.btn-outline{display:inline-block;margin-top:46px;border:2px solid var(--white);padding:7px 36px;font-size:14px;line-height:20px;letter-spacing:2px}
.hero-arrow{position:absolute;top:284px;font-size:24px;color:#9a9a9a}
.hero-arrow.prev{left:94px}.hero-arrow.next{right:94px}
.dots{display:flex;gap:5px;justify-content:center}
.dot{width:10px;height:10px;border-radius:50%;border:1.5px solid var(--white)}
.dot.active{background:var(--white)}
.hero .dots{position:absolute;top:474px;left:0;right:0}

/* services */
.services{height:357px;padding-top:38px}
.service-grid{display:flex;justify-content:space-between;margin-top:64px}
.service{width:490px;text-align:center}
.service-icon{width:80px;height:80px;border-radius:50%;background:var(--orange);margin:0 auto;display:flex;align-items:center;justify-content:center}
.service h3{font-family:"Montserrat",sans-serif;font-weight:700;font-size:17px;line-height:22px;letter-spacing:2.5px;margin-top:34px}
.service p{font-size:12.5px;margin-top:4px;white-space:nowrap}

/* about */
.about{height:468px;padding-top:26px}
.about-row{display:flex;justify-content:space-between;margin-top:28px}
.about-photo{width:494px;height:287px;border-radius:8px;background:linear-gradient(180deg,#f0a430 0%,#c77418 45%,#5a3210 75%,#0c0a08 100%)}
.about-text{width:494px}
.about-text p{font-size:12.5px;line-height:1.45;margin-bottom:8px}
.about-text hr{border:0;border-top:1px solid var(--line);margin:4px 0 22px}
.btn{display:inline-block;background:var(--orange);color:var(--white);padding:7px 14px;border-radius:3px;font-size:14px;line-height:20px}

/* testimonial */
.testimonial{height:304px;background:linear-gradient(180deg,#3b2a18 0%,#1e1a16 50%,#3a2816 100%);text-align:center;padding-top:58px}
.avatar{width:60px;height:60px;border-radius:50%;border:4px solid var(--white);background:linear-gradient(#7fc6c9,#3d8c95);margin:0 auto}
.quote{width:864px;margin:14px auto 0;font-size:15px;line-height:1.5}
.quote .mark{font-family:"Merriweather",serif;font-size:22px;line-height:1}
.client{font-size:12.5px;margin-top:14px}
.stars{display:flex;justify-content:center;margin:2px 0 8px}

/* team */
.team{height:408px;padding-top:69px}
.team-card{width:492px;height:291px;margin:0 auto;border:1px solid var(--line);border-radius:4px;overflow:hidden;text-align:center}
.team-photo{height:148px;background:linear-gradient(180deg,#e89a2c 0%,#b46618 55%,#2a1a0c 100%)}
.monogram{width:60px;height:60px;border-radius:50%;background:var(--white);color:var(--orange);font-family:"Montserrat",sans-serif;font-weight:700;font-size:23px;line-height:60px;margin:-30px auto 0;position:relative}
.team-name{font-family:"Montserrat",sans-serif;font-weight:700;font-size:21px;line-height:28px;letter-spacing:3px;margin-top:2px}
.team-role{color:var(--orange);font-family:"Montserrat",sans-serif;font-weight:600;font-size:11.5px;letter-spacing:3px}
.team-card p{font-size:12.5px;line-height:1.55;margin-top:4px}

/* contact */
.contact{height:537px;padding-top:57px}
.contact-row{display:flex;justify-content:space-between;margin-top:30px}
.contact-info{width:494px}
.contact-info h3{font-family:"Montserrat",sans-serif;font-weight:700;font-size:20px;line-height:26px;letter-spacing:2.5px}
.contact-info > p{font-size:12.5px;line-height:1.45;margin-top:2px}
.info-list{margin-top:12px}
.info-item{border-top:1px solid var(--line);display:flex;gap:24px;padding:14px 0;font-size:12.5px;line-height:1.5}
.info-item:last-child{border-bottom:1px solid var(--line)}
.info-item svg{flex:none}
.contact-form{width:494px}
.contact-form label{display:block;font-weight:600;font-size:12px;line-height:18px}
.field{background:var(--white);color:#999;border-radius:3px;height:26px;padding:3px 12px;font-size:12px;line-height:20px;margin-bottom:16px}
.field.area{height:114px}

/* footer */
.footer{height:62px;background:var(--bg-dark)}
.footer .container{display:flex;justify-content:space-between;align-items:center;font-size:12.5px}
.social{display:flex;gap:16px}
.social span{width:9px;height:9px;border-radius:50%;background:var(--white)}
</style>
</head>
<body>
<div class="page">

<section class="hero">
  <div class="hero-photo" role="img" aria-label="Excavator silhouetted against a glowing sunset sky behind a fine lattice overlay"></div>
  <nav class="nav">
    <div class="brand">Mosk trail</div>
    <ul class="nav-links"><li>ABOUT</li><li>SERVICES</li><li>TESTIMONIALS</li><li>WHO</li><li>CONTACT</li></ul>
  </nav>
  <span class="hero-arrow prev">‹</span><span class="hero-arrow next">›</span>
  <div class="hero-copy">
    <div class="hero-kicker">WELCOME TO</div>
    <h1 class="hero-title">MOSK TRAIL</h1>
    <div class="btn-outline">OUR SERVICES</div>
  </div>
  <div class="dots"><span class="dot active"></span><span class="dot"></span><span class="dot"></span></div>
</section>

<section class="services">
  <div class="container">
    <h2 class="section-title">OUR SERVICES</h2>
    <div class="service-grid">
      <div class="service">
        <div class="service-icon"><svg width="40" height="40" viewBox="0 0 44 44" fill="none" stroke="#fff" stroke-width="3" stroke-linejoin="round"><path d="M8 14l14-7 14 7v16l-14 7-14-7z"/><path d="M8 14l14 7 14-7M22 21v16"/></svg></div>
        <h3>WE PROCURE AND DISPOSE</h3>
        <p>We procure and dispose of earthmoving construction equipment</p>
      </div>
      <div class="service">
        <div class="service-icon"><svg width="42" height="42" viewBox="0 0 48 48" fill="none" stroke="#fff" stroke-width="4" stroke-linecap="round"><circle cx="20" cy="20" r="12"/><path d="M29 29l11 11M20 14v12M14 20h12"/></svg></div>
        <h3>FIND CONSTRUCTION EQUIPMENTS</h3>
        <p>We also find construction equipment for our customers using our global contacts</p>
      </div>
    </div>
  </div>
</section>

<section class="about">
  <div class="container">
    <h2 class="section-title">ABOUT US</h2>
    <div class="about-row">
      <div class="about-photo" role="img" aria-label="Bulldozer silhouetted against an orange sunset"></div>
      <div class="about-text">
        <p>Lorem ipsum dolor sit amet, consectetur adipiscing elit. Donec a tempor eros. Pellentesque elementum nulla sed justo tempor posuere sit amet sit amet ligula. Curabitur felis nibh, imperdiet eu erat non, luctus cursus lectus. Donec maximus diam leo, sed fringilla nisl auctor eget. Donec dictum neque est, ac faucibus ex blandit a. Curabitur felis nibh, imperdiet eu erat non, luctus cursus lectus. Donec maximus diam leo, sed fringilla nisl auctor eget. Donec dictum neque est, ac faucibus ex blandit a.</p>
        <p>Lorem ipsum dolor sit amet, consectetur adipiscing elit. Donec a tempor eros. Pellentesque elementum nulla sed justo tempor posuere sit amet sit amet ligula. Curabitur felis nibh, imperdiet eu erat non, luctus cursus lectus. Donec maximus diam leo, sed fringilla nisl auctor eget. Donec dictum neque est, ac faucibus ex blandit a.</p>
        <hr>
        <span class="btn">CONTACT US</span>
      </div>
    </div>
  </div>
</section>

<section class="testimonial" role="img" aria-label="Dim band of excavators at dusk behind a client testimonial">
  <div class="avatar" role="img" aria-label="Client avatar"></div>
  <p class="quote"><span class="mark">“</span> Lorem ipsum dolor sit amet, ea sea dolore ubique, duo consul nominavi eu. Illum partem vidisse no vix. Id unum scribentur est. Posse luptatum vituperatoribus et quo, usu cu veri nominavi scripserit, eum cu natum iuvaret. <span class="mark">”</span></p>
  <div class="client">Clint one</div>
  <div class="stars">
    <svg width="60" height="12" viewBox="0 0 60 12" fill="var(--star)"><path id="s" d="M6 0l1.8 3.9 4.2.5-3.1 2.9.8 4.2L6 9.4 2.3 11.5l.8-4.2L0 4.4l4.2-.5z"/><use href="#s" x="12"/><use href="#s" x="24"/><use href="#s" x="36"/><path d="M54 0v9.4l-3.7 2.1.8-4.2L48 4.4l4.2-.5z"/></svg>
  </div>
  <div class="dots"><span class="dot active"></span><span class="dot"></span><span class="dot"></span><span class="dot"></span></div>
</section>

<section class="team">
  <div class="team-card">
    <div class="team-photo" role="img" aria-label="Bulldozer silhouetted against a sunset"></div>
    <div class="monogram">MT</div>
    <div class="team-name">DANIEL REEVES</div>
    <div class="team-role">MANAGING DIRECTOR</div>
    <p>daniel@mosktrail.com.au<br>0400 218 764</p>
  </div>
</section>

<section class="contact">
  <div class="container">
    <h2 class="section-title">CONTACT US</h2>
    <div class="contact-row">
      <div class="contact-info">
        <h3>GET IN TOUCH</h3>
        <p>Lorem ipsum dolor sit amet, consectetur adipiscing elit. Curabitur eget leo at velit imperdiet varius. In eu ipsum vitae velit congue iaculis vitae at risus. Lorem ipsum dolor sit amet, consectetur adipiscing elit.</p>
        <div class="info-list">
          <div class="info-item"><svg width="14" height="20" viewBox="0 0 14 20"><path d="M7 0a7 7 0 0 0-7 7c0 5 7 13 7 13s7-8 7-13a7 7 0 0 0-7-7z" fill="var(--orange)"/><circle cx="7" cy="7" r="2.6" fill="var(--bg)"/></svg><div>ADDRESS<br>Address line one<br>Address line two<br>Address line two<br>Address line two</div></div>
          <div class="info-item"><svg width="20" height="20" viewBox="0 0 20 20"><rect width="20" height="20" rx="3" fill="var(--orange)"/><path d="M6 4l2.5 3-1.5 1.5c.8 1.8 2.2 3.2 4 4L12.5 11l3 2.5-1.5 2.5C9 15.5 4.5 11 4 5.5z" fill="var(--bg)"/></svg><div>0400 218 764</div></div>
          <div class="info-item"><svg width="22" height="16" viewBox="0 0 22 16"><rect width="22" height="16" rx="2" fill="var(--orange)"/><path d="M1 2l10 7 10-7" fill="none" stroke="var(--bg)" stroke-width="2"/></svg><div>daniel@mosktrail.com.au</div></div>
        </div>
      </div>
      <form class="contact-form">
        <label>Name:</label><div class="field">Enter name</div>
        <label>Email:</label><div class="field">Enter email</div>
        <label>Subject:</label><div class="field">Enter subject</div>
        <label>Message:</label><div class="field area">Enter message</div>
        <span class="btn">Send Message</span>
      </form>
    </div>
  </div>
</section>

<footer class="footer">
  <div class="container">
    <div>© 2018 @Mosk trail.</div>
    <div class="social" aria-label="Social links"><span></span><span></span><span></span><span></span></div>
  </div>
</footer>

</div>
</body>
</html>
```